Pizza Box 10" x 10" - color: White

Custom design, utilizing CrustVarto Logo and include the following information on the Pizza Box:

1. Custom Crafted Pizza with Quality Ingredients.
2. [....Get Your GAME ON] to be placed on the front flap and seen when the
box is opened.
3. You"ll miss 100% of the Pizza you don't eat.

4. Visit www.plenovacartons.example for additional design resource information. Go to site and then click on ORDERING to access.

5. The 10" x 10" Pizza Box is to be in the color WHITE.
6. Use colors Black and Red. no generic images. no food pics. I am looking for a clean and cool design.

Target Market(s)

Age 16 - 36 years

Industry/Entity Type

American Restaurant

Font styles to use
Sans Serif

Colors
ec1f27
000000
ffffff

Requirements
Must have
• Color Red and Black.
• Logo on Top and all sides of the Pizza Box.
Nice to have
• A Creative design that does not look generic.
Should not have
• No food images.

```html
<!DOCTYPE html>
<html lang="en">
<head>
<meta charset="utf-8">
<title>CrustVarto Pizza Box</title>
<link href="https://fonts.googleapis.com/css2?family=Archivo+Black&family=Oswald:wght@500;700&display=swap" rel="stylesheet">
<style>
  :root {
    --red: #ec1f27;
    --black: #000000;
    --white: #ffffff;
    --board: #f6f0e8;
    --stage: #e9e6e2;
    --sketch: #efb9b3;
  }
  * { box-sizing: border-box; margin: 0; padding: 0; }
  html, body { width: 1200px; height: 938px; overflow: hidden; background: var(--stage); }
  .canvas { position: relative; width: 1200px; height: 938px; }

  /* shared logo */
  .logo-pill {
    display: flex; align-items: center; gap: 10px;
    background: var(--white); border: 3px solid var(--black);
    border-radius: 30px; padding: 6px 18px; white-space: nowrap;
  }
  .logo-mark { width: 26px; height: 26px; border-radius: 50%; background: var(--black); flex: none; }
  .logo-name { font-family: "Archivo Black", sans-serif; font-size: 24px; color: var(--black); }

  /* left side panel */
  .side-panel {
    position: absolute; left: 180px; top: 30px; width: 130px; height: 700px;
    background: var(--red); overflow: hidden;
  }
  .side-strip {
    position: absolute; left: -285px; top: 285px; width: 700px; height: 130px;
    transform: rotate(90deg);
    display: flex; align-items: center; gap: 28px; padding: 0 24px;
  }
  .side-strip .logo-pill { flex: none; padding: 10px 20px; }
  .side-tagline {
    font-family: "Oswald", sans-serif; font-weight: 700; font-size: 44px; color: var(--black);
    white-space: nowrap;
  }

  /* lid */
  .lid {
    position: absolute; left: 320px; top: 30px; width: 700px; height: 700px;
    background: var(--board); overflow: hidden;
  }
  .sketch-area {
    position: absolute; top: 20px; height: 440px;
    background: radial-gradient(ellipse at 50% 45%, var(--sketch) 0%, rgba(239,185,179,.35) 55%, rgba(246,240,232,0) 80%);
  }
  .sketch-left { left: 0; width: 195px; }
  .sketch-right { right: 0; width: 195px; }

  .flame-area {
    position: absolute; left: 0; bottom: 0; width: 100%; height: 250px;
    background: linear-gradient(180deg, rgba(236,31,39,0) 0%, rgba(236,31,39,.45) 35%, rgba(236,31,39,.8) 65%, var(--red) 100%);
  }

  .brand-band {
    position: absolute; left: 195px; top: 0; width: 310px; height: 560px;
    background: var(--red);
  }
  .brand-band .logo-pill { position: absolute; left: 24px; top: 28px; width: 262px; justify-content: center; }

  .slogan-box {
    position: absolute; left: 20px; top: 100px; width: 270px; height: 420px;
    background: var(--black); border-radius: 18px;
    display: flex; flex-direction: column; justify-content: center; align-items: center;
    font-family: "Archivo Black", sans-serif; color: var(--white); text-align: center;
    line-height: 1.08;
  }
  .slogan-box .small { font-size: 32px; }
  .slogan-box .big { font-size: 52px; }

  .order-line {
    position: absolute; left: 0; bottom: 26px; width: 100%; text-align: center;
    font-family: "Archivo Black", sans-serif; font-size: 20px; color: var(--white); letter-spacing: .5px;
  }

  /* front flap */
  .front-flap {
    position: absolute; left: 320px; top: 740px; width: 700px; height: 130px;
    background: var(--red); display: flex; align-items: center; gap: 24px; padding: 0 22px;
  }
  .front-flap .logo-pill { flex: none; padding: 10px 20px; }
  .game-on {
    flex: 1; height: 96px; background: var(--black);
    display: flex; align-items: center; justify-content: center;
    font-family: "Oswald", sans-serif; font-weight: 700; font-size: 44px; color: var(--white);
    white-space: nowrap;
  }
</style>
</head>
<body>
<main class="canvas">
  <section class="side-panel">
    <div class="side-strip">
      <div class="logo-pill"><span class="logo-mark"></span><span class="logo-name">CrustVarto</span></div>
      <span class="side-tagline">....Get Your GAME ON</span>
    </div>
  </section>

  <section class="lid">
    <div class="sketch-area sketch-left" role="img" aria-label="Red line sketches of pepper, herbs, tomato and pizza slice"></div>
    <div class="sketch-area sketch-right" role="img" aria-label="Red line sketches of rolling pin, pizza slice, tomato and chili"></div>
    <div class="flame-area" role="img" aria-label="Red flame pattern rising from the bottom edge"></div>

    <div class="brand-band">
      <div class="logo-pill"><span class="logo-mark"></span><span class="logo-name">CrustVarto</span></div>
      <div class="slogan-box">
        <span class="small">You"ll miss</span>
        <span class="big">100%</span>
        <span class="big">of the</span>
        <span class="small">Pizza you</span>
        <span class="small">don't eat.</span>
      </div>
    </div>

    <p class="order-line">Oder Now: 555-014-2290</p>
  </section>

  <section class="front-flap">
    <div class="logo-pill"><span class="logo-mark"></span><span class="logo-name">CrustVarto</span></div>
    <div class="game-on">....Get Your GAME ON</div>
  </section>
</main>
</body>
</html>
```